Modern, profession Order Insert Card for Head Shop/Smoke shop

We are looking for a modern design for our Order Insert cards where we will have some text thanking the customer for their order.
The design needs to be professional and modern, showing our logo (SVG attached) and our website URL.
Our eCommerce store sells "head shop" items, things like bongs, rolling papers, cbd products, disposable vapes, etc.
I have uploaded 2 versions of our logo, one featuring the colour of green we use across our brand, a black logo or the logo can be inverted to be a white logo on a black background.
Target Market(s)
The websites target audience is anyone needing accessories or tools to consume medicinal marijuana/the consumers favourite herbs or any one in the vaping community.
Contact Information for Business Card
Website URL, Space for a small thank you note and our logo.
Look and feel

```html
<!DOCTYPE html>
<html lang="en">
<head>
<meta charset="utf-8">
<title>Leafline Supply – Order Insert Card</title>
<link rel="stylesheet" href="https://fonts.googleapis.com/css2?family=Oswald:wght@700&family=Montserrat:wght@500;600&family=Dancing+Script:wght@700&display=swap">
<style>
  :root {
    --backdrop: #262626;
    --card-green: #6f952f;
    --accent-lime: #a3d94a;
    --ornament-tint: rgba(214, 230, 190, 0.55);
    --ink-white: #ffffff;
  }
  html, body {
    margin: 0;
    padding: 0;
    overflow: hidden;
  }
  body {
    width: 1200px;
    height: 1015px;
    background: var(--backdrop);
    position: relative;
  }
  .insert-card {
    position: absolute;
    left: 110px;
    top: 227px;
    width: 980px;
    height: 560px;
    background: var(--card-green);
    overflow: hidden;
  }
  .ornament {
    position: absolute;
    border-radius: 50%;
  }
  .ornament--top-right {
    right: -120px;
    top: -140px;
    width: 420px;
    height: 520px;
    background: radial-gradient(circle at 40% 55%, var(--ornament-tint) 0%, rgba(214,230,190,0.25) 55%, transparent 72%);
  }
  .ornament--left {
    left: -150px;
    top: 120px;
    width: 380px;
    height: 380px;
    background: radial-gradient(circle at 55% 50%, var(--ornament-tint) 0%, rgba(214,230,190,0.25) 55%, transparent 72%);
  }
  .ornament--bottom {
    left: 120px;
    bottom: -230px;
    width: 440px;
    height: 400px;
    background: radial-gradient(circle at 50% 40%, var(--ornament-tint) 0%, rgba(214,230,190,0.25) 55%, transparent 72%);
  }
  .brand {
    position: absolute;
    left: 0;
    right: 0;
    top: 118px;
    display: flex;
    justify-content: center;
    align-items: center;
    gap: 14px;
  }
  .brand__dot {
    width: 34px;
    height: 34px;
    border-radius: 50%;
    background: var(--ink-white);
  }
  .brand__name {
    font-family: "Montserrat", sans-serif;
    font-weight: 600;
    font-size: 30px;
    letter-spacing: 1px;
    color: var(--ink-white);
  }
  .thanks {
    position: absolute;
    left: 0;
    right: 0;
    top: 190px;
    text-align: center;
  }
  .thanks__headline {
    margin: 0;
    font-family: "Oswald", sans-serif;
    font-weight: 700;
    font-size: 118px;
    line-height: 1;
    letter-spacing: 1px;
    color: var(--accent-lime);
  }
  .thanks__note {
    margin: -42px 0 0 40px;
    font-family: "Dancing Script", cursive;
    font-weight: 700;
    font-size: 84px;
    line-height: 1;
    color: var(--ink-white);
  }
  .website {
    position: absolute;
    left: 0;
    right: 0;
    bottom: 78px;
    text-align: center;
    font-family: "Montserrat", sans-serif;
    font-weight: 500;
    font-size: 24px;
    letter-spacing: 1px;
    color: var(--ink-white);
  }
</style>
</head>
<body>
  <main class="insert-card">
    <div class="ornament ornament--top-right" role="img" aria-label="Decorative light green swirl pattern"></div>
    <div class="ornament ornament--left" role="img" aria-label="Decorative light green swirl pattern"></div>
    <div class="ornament ornament--bottom" role="img" aria-label="Decorative light green swirl pattern"></div>

    <div class="brand">
      <span class="brand__dot"></span>
      <span class="brand__name">LEAFLINE SUPPLY</span>
    </div>

    <div class="thanks">
      <h1 class="thanks__headline">THANK YOU</h1>
      <p class="thanks__note">for your order</p>
    </div>

    <p class="website">www.leaflinesupply.com</p>
  </main>
</body>
</html>
```